Design flyer for CLOM

Cedar Lamp Outreach Ministry (CLOM)
• The praise and worship team of RKTC
• The vision is to support members become the praise of God
• The mandate is to help members actualize the glorious privilege to be His praise
• Organize and coordinate Crosswind Friday Rally Night and Rivers of Gladness
• Goal is to enable members learn to worship God in spirit and in truth
• CLOM is made up of chapter praise team DRTSK praise team, the united Anthem Chorale and the Harmony Academy
• The goal is to manifest God’s glory as we worship Him in spirit and in truth

Join Cedar Lamp Outreach Ministry

```html
<!DOCTYPE html>
<html lang="en">
<head>
<meta charset="utf-8">
<title>Cedar Lamp Outreach Ministry</title>
<link rel="stylesheet" href="https://fonts.googleapis.com/css2?family=Ubuntu:wght@400;500&display=swap">
<style>
  :root {
    --top-bar: #1d4f93;
    --wave-light: #b9dcf7;
    --wave-mid: #a9b8f4;
    --wave-deep: #8f86ef;
    --heading-white: #f4f4ff;
    --accent-violet: #8a78ee;
    --logo-blue: #2c5f96;
    --sky-top: #eaf4fc;
    --sky-mid: #8cc4ec;
    --sky-low: #d7ecfa;
    --grass: #3fae2a;
    --grass-dark: #2c8c1c;
    --page: #ffffff;
  }
  * { margin: 0; padding: 0; box-sizing: border-box; }
  html, body { width: 929px; height: 1200px; overflow: hidden; background: var(--page); }
  .flyer {
    position: relative;
    width: 929px; height: 1200px;
    overflow: hidden;
    font-family: "Ubuntu", sans-serif;
    background: var(--page);
  }
  .top-bar { position: absolute; left: 0; top: 0; width: 100%; height: 9px; background: var(--top-bar); }
  .wave { position: absolute; left: 0; top: 0; width: 929px; height: 560px; }
  .landscape {
    position: absolute; left: 0; top: 760px; width: 929px; height: 440px;
    background:
      linear-gradient(to bottom, rgba(255,255,255,0) 0%, var(--sky-mid) 30%, var(--sky-low) 62%, #f4faff 78%, var(--grass) 80%, var(--grass-dark) 100%);
  }
  .brand {
    position: absolute; left: 470px; top: 30px;
    display: flex; align-items: center; gap: 14px;
  }
  .brand-mark {
    width: 130px; height: 130px; border-radius: 50%;
    background: var(--logo-blue);
  }
  .brand-name {
    font-size: 26px; font-weight: 500; color: var(--logo-blue);
    line-height: 1.15; width: 190px;
  }
  .intro {
    position: absolute; left: 9px; top: 164px; width: 660px;
    color: var(--heading-white);
  }
  .intro-title { font-size: 27px; font-weight: 500; margin-bottom: 26px; }
  .intro-list { list-style: none; font-size: 23px; line-height: 34px; font-weight: 500; }
  .goals {
    position: absolute; left: 380px; top: 512px; width: 500px;
    text-align: center; color: var(--accent-violet);
    font-size: 23px; font-weight: 500; line-height: 34px;
    list-style: none;
  }
  .goals li { margin-bottom: 34px; }
</style>
</head>
<body>
<div class="flyer">
  <div class="landscape" role="img" aria-label="Bright sky with soft clouds, a lone green tree and a grassy meadow"></div>

  <svg class="wave" viewBox="0 0 929 560" aria-hidden="true">
    <defs>
      <linearGradient id="waveFill" x1="0" y1="0" x2="0.4" y2="1">
        <stop offset="0" stop-color="var(--wave-light)"/>
        <stop offset="0.45" stop-color="var(--wave-mid)"/>
        <stop offset="0.8" stop-color="var(--wave-deep)"/>
        <stop offset="1" stop-color="#ffffff" stop-opacity="0"/>
      </linearGradient>
    </defs>
    <path d="M0,58 C300,40 620,110 760,160 C840,190 900,210 929,212 C880,300 760,360 620,400 C420,460 200,520 0,540 Z" fill="url(#waveFill)"/>
    <path d="M0,58 C300,40 620,110 760,160 C840,190 900,210 929,212" fill="none" stroke="#ffffff" stroke-opacity="0.7" stroke-width="3"/>
    <path d="M560,300 C700,290 860,250 929,212" fill="none" stroke="#ffffff" stroke-opacity="0.6" stroke-width="2"/>
  </svg>

  <div class="top-bar"></div>

  <div class="brand">
    <div class="brand-mark"></div>
    <div class="brand-name">Riverkeep Tabernacle Church</div>
  </div>

  <section class="intro">
    <h1 class="intro-title">Cedar Lamp Outreach Ministry (CLOM)</h1>
    <ul class="intro-list">
      <li>- The praise and worship team of RKTC</li>
      <li>- The vision is to support members become the praiseof God</li>
      <li>- The mandate is to help members actualize the glorious privilege to be His praise</li>
      <li>- Organize and coordinate Crosswind Friday Rally Night and &nbsp;Rivers of Gladness</li>
    </ul>
  </section>

  <ul class="goals">
    <li>- Goal is to enable members learn to<br>worship God in spirit and in truth</li>
    <li>- CLOM is made up of chapter praise team<br>DRTSK praise team,<br>the united Anthem Chorale and the Harmony Academy</li>
    <li>- The goal is to manifest God’s glory as we<br>worship Him in spirit and in truth</li>
  </ul>
</div>
</body>
</html>
```